Challenge Graphics for Social Media

I want to create 9 social media graphics (new Instagram size 4:5 (1080 x 1350 pixels) focusing on our next 12-Week Amber Broth Quest on May 4th. Use any of the pics in the dropbox, NO RANDOM STOCK PHOTOGRAPHY. For the color scheme of the graphics, they should all be complementary to the green smoothie book attached.
You should add a copy of the book AND a bottle of the green smoothie gummies to each graphic. Note: all the pics from the dropbox are also attached here. The text for these graphics are one of the 2 options:
Summer is 2 Months Away!
Join the 12-Week Amber Broth Quest on May 4th!
Lose Up to 15lbs in 10 Days!
Get Your Summer Body Ready!
Join the 12-Week Amber Broth Quest (with Gummies)
Begins Monday May 4th

```html
<!DOCTYPE html>
<html lang="en">
<head>
<meta charset="utf-8">
<title>Amber Broth Quest – Social Graphics</title>
<link href="https://fonts.googleapis.com/css2?family=Oswald:wght@400;500;600;700&family=Poppins:wght@500;600;700;800&display=swap" rel="stylesheet">
<style>
:root{
  --canvas:#3d3d3d;
  --green-dark:#2b7a35;
  --green-light:#6cc33f;
  --blue:#1a86d0;
  --blue-deep:#0f6fb8;
  --brown:#2e1a16;
  --ink:#222;
  --mint:#cfe6d2;
  --white:#fff;
  --paper:#f3f3f3;
  --geo:'Poppins',sans-serif;
  --cond:'Oswald',sans-serif;
}
*{box-sizing:border-box;margin:0;padding:0}
html,body{width:980px;height:1200px;overflow:hidden;background:var(--canvas)}
.board{position:relative;width:980px;height:1200px}
.tile{position:absolute;width:272px;height:340px;overflow:hidden;background:var(--white)}
.c1{left:48px}.c2{left:348px}.c3{left:650px}
.r1{top:58px}.r2{top:424px}.r3{top:794px}
.abs{position:absolute;white-space:nowrap}
.geo{font-family:var(--geo);font-weight:800;line-height:1}
.cond{font-family:var(--cond);font-weight:600;line-height:1;text-transform:uppercase}
.tall{transform:scaleY(1.18);transform-origin:center top}
.center{left:0;right:0;text-align:center}
.white{color:var(--white)}.dg{color:var(--green-dark)}.lg{color:var(--green-light)}.bl{color:var(--blue)}.br{color:var(--brown)}
.photo{position:absolute;background:linear-gradient(160deg,#c9a7b8,#8d6a70 55%,#3a2a2c)}
.photo.dots{background:linear-gradient(160deg,#e8e4e2,#9a8f8f 45%,#2a2526)}
.photo.outdoor{background:linear-gradient(160deg,#7f9a6a,#c8a2b6 50%,#e9c4d6)}
.bottle{position:absolute;border-radius:10px 10px 6px 6px;background:linear-gradient(180deg,#2d7d35 0 14%,#ece9e4 14% 100%)}
.book{position:absolute;border-radius:3px;background:linear-gradient(180deg,#f4f6f2 0 38%,#7fbf4a 38%,#3b8a3a 85%,#1a86d0 85%)}

.loss-band{position:absolute;left:0;right:0;top:282px;bottom:0;background:var(--white)}
.loss-band.mint{background:var(--mint)}
.loss-band.forest{background:var(--green-dark)}
.loss-frame{position:absolute;left:18px;right:18px;top:17px;bottom:-2px;border:1.5px solid #9a9a9a;border-bottom:none;border-radius:6px 6px 0 0}
.forest .loss-frame{border-color:var(--white)}
.loss-top{position:absolute;top:-11px;left:50%;transform:translateX(-50%);padding:0 7px;font-family:var(--geo);font-weight:500;font-size:18px;line-height:20px;white-space:nowrap;color:var(--ink);background:var(--white)}
.mint .loss-top{background:var(--mint)}
.forest .loss-top{background:var(--green-dark);color:var(--white)}
.loss-main{position:absolute;top:10px;left:0;right:0;text-align:center;font-family:var(--geo);font-weight:800;font-size:21.5px;line-height:24px;white-space:nowrap}
</style>
</head>
<body>
<main class="board">

<!-- 1 -->
<section class="tile c1 r1">
  <div class="abs center geo dg" style="top:12px;font-size:35px">SUMMER IS</div>
  <div class="abs" style="left:0;right:0;top:50px;height:50px;background:var(--green-light)"></div>
  <div class="abs center geo white" style="top:56px;font-size:40px">2 MONTHS</div>
  <div class="abs geo bl" style="left:18px;top:106px;font-size:35px">AWAY!</div>
  <div class="abs" style="left:18px;top:146px;width:150px;height:1px;background:#bbb"></div>
  <div class="abs cond" style="left:18px;top:154px;width:150px;text-align:center;font-size:20px;line-height:22px;color:var(--ink)">JOIN THE <span class="dg">12-WEEK</span><br><span class="dg">AMBER BROTH</span><br>QUEST ON</div>
  <div class="abs cond white" style="left:18px;top:225px;width:122px;height:57px;background:var(--green-dark);border-radius:10px 10px 0 0;text-align:center;padding-top:10px;font-size:30px">MAY 4TH!</div>
  <div class="abs" style="left:0;right:0;top:278px;height:4px;background:var(--green-dark)"></div>
  <div class="bottle" role="img" aria-label="Gummies supplement bottle" style="left:165px;top:110px;width:82px;height:168px"></div>
  <div class="loss-band"><div class="loss-frame"><span class="loss-top">LOSE UP TO</span><div class="loss-main bl">15LBS IN 10 DAYS!</div></div></div>
</section>

<!-- 2 -->
<section class="tile c2 r1">
  <div class="photo dots" role="img" aria-label="Host in polka-dot top holding gummies bottle" style="left:135px;top:16px;width:137px;height:234px"></div>
  <div class="abs geo dg" style="left:18px;top:16px;font-size:26px">GET YOUR</div>
  <div class="abs cond bl" style="left:18px;top:42px;font-size:44px;font-weight:700">SUMMER</div>
  <div class="abs geo lg" style="left:18px;top:90px;font-size:33px">BODY</div>
  <div class="abs geo lg" style="left:18px;top:122px;font-size:29px">READY!</div>
  <div class="abs" style="left:18px;top:157px;width:112px;height:1px;background:#bbb"></div>
  <div class="abs cond" style="left:18px;top:170px;font-size:17.5px;line-height:20px;color:var(--ink)">JOIN THE 12-WEEK<br>AMBER BROTH<br>QUEST</div>
  <div class="abs geo dg" style="left:18px;top:234px;font-size:8.5px;font-weight:600">(WITH GUMMIES)</div>
  <div class="abs" style="left:0;right:0;top:250px;height:32px;background:var(--green-dark)"></div>
  <div class="abs center geo white" style="top:259px;font-size:15px;font-weight:700">BEGINS MONDAY MAY 4TH</div>
  <div class="loss-band"><div class="loss-frame"><span class="loss-top">LOSE UP TO</span><div class="loss-main bl">15LBS IN 10 DAYS!</div></div></div>
</section>

<!-- 3 -->
<section class="tile c3 r1">
  <div class="photo outdoor" role="img" aria-label="Host in pink outfit laughing, holding gummy and bottle" style="left:0;top:0;width:272px;height:282px"></div>
  <div class="abs" style="left:0;right:0;top:150px;height:132px;background:linear-gradient(180deg,rgba(255,255,255,0),#fff 35%)"></div>
  <div class="abs center geo lg" style="top:174px;font-size:25px">SUMMER IS</div>
  <div class="abs center cond bl" style="top:200px;font-size:36px;font-weight:700">2 MONTHS AWAY!</div>
  <div class="abs center geo" style="top:244px;font-size:10.5px;font-weight:600;line-height:15px;color:var(--ink)">JOIN THE 12-WEEK AMBER BROTH<br>QUEST ON <span class="lg">MAY 4TH!</span></div>
  <div class="loss-band forest"><div class="loss-frame"><span class="loss-top">LOSE UP TO</span><div class="loss-main white">15LBS IN 10 DAYS!</div></div></div>
</section>

<!-- 4 -->
<section class="tile c1 r2">
  <div class="abs" style="left:0;right:0;top:0;height:112px;background:var(--green-dark)"></div>
  <div class="abs" style="left:0;right:0;top:112px;height:170px;background:var(--paper)"></div>
  <div class="abs center geo white" style="top:14px;font-size:27px">GET YOUR</div>
  <div class="abs center geo lg" style="top:44px;font-size:41px">SUMMER</div>
  <div class="abs center geo white" style="top:88px;font-size:27px;height:24px;overflow:hidden">BODY READY!</div>
  <div class="bottle" role="img" aria-label="Gummies supplement bottle" style="left:36px;top:122px;width:68px;height:150px"></div>
  <div class="abs geo" style="left:126px;top:128px;font-size:12.5px;font-weight:700;line-height:16.5px;color:var(--ink)">JOIN THE 12-WEEK<br>AMBER BROTH<br>QUEST</div>
  <div class="abs geo" style="left:126px;top:181px;font-size:9.5px;font-weight:500;color:var(--ink)">(WITH GUMMIES)</div>
  <div class="abs geo" style="left:126px;top:206px;font-size:7px;writing-mode:vertical-rl;transform:rotate(180deg);color:var(--ink)">BEGINS</div>
  <div class="abs cond dg" style="left:136px;top:198px;font-size:35px;font-weight:700">MONDAY</div>
  <div class="abs cond dg" style="left:126px;top:236px;font-size:35px;font-weight:700">MAY 4TH</div>
  <div class="loss-band mint"><div class="loss-frame"><span class="loss-top">LOSE UP TO</span><div class="loss-main br">15LBS IN 10 DAYS!</div></div></div>
</section>

<!-- 5 -->
<section class="tile c2 r2">
  <svg class="abs" style="left:0;top:0" width="272" height="282" viewBox="0 0 272 282" aria-hidden="true">
    <defs><linearGradient id="sky" x1="0" y1="0" x2="1" y2="1"><stop offset="0" stop-color="#1a86d0"/><stop offset="1" stop-color="#0f6fb8"/></linearGradient></defs>
    <rect width="272" height="282" fill="#fff"/>
    <path d="M0 0H272V128Q150 168 0 140Z" fill="url(#sky)"/>
    <path d="M0 140Q150 168 272 128V134Q150 176 0 148Z" fill="#6cc33f"/>
  </svg>
  <div class="abs center geo white" style="top:14px;font-size:27px">SUMMER IS</div>
  <div class="abs center cond white" style="top:40px;font-size:60px;font-weight:700">2 MONTHS</div>
  <div class="abs center geo white" style="top:104px;font-size:24px">AWAY!</div>
  <div class="book" role="img" aria-label="Cleanse recipe book cover" style="left:158px;top:140px;width:92px;height:140px"></div>
  <div class="abs cond" style="left:18px;top:166px;font-size:18px;line-height:22px;color:var(--ink)">JOIN THE <span class="dg">12-WEEK</span><br>AMBER BROTH<br>QUEST ON</div>
  <div class="abs cond dg" style="left:18px;top:238px;font-size:33px;font-weight:700">MAY 4TH!</div>
  <div class="loss-band mint"><div class="loss-frame"><span class="loss-top">LOSE UP TO</span><div class="loss-main br">15LBS IN 10 DAYS!</div></div></div>
</section>

<!-- 6 -->
<section class="tile c3 r2" style="background:var(--green-dark)">
  <div class="photo outdoor" role="img" aria-label="Host in pink outfit laughing, holding a gummy" style="left:150px;top:0;width:122px;height:282px;background:linear-gradient(160deg,#3e8a3e,#c995b1 40%,#e6b3cc)"></div>
  <div class="abs geo white" style="left:18px;top:14px;font-size:27px">GET YOUR</div>
  <div class="abs cond white" style="left:18px;top:40px;font-size:44px;font-weight:700">SUMMER</div>
  <div class="abs cond white" style="left:18px;top:90px;font-size:31px;font-weight:400">BODY READY!</div>
  <div class="abs" style="left:0;top:130px;width:196px;height:78px;background:var(--green-light)"></div>
  <div class="abs geo white" style="left:19px;top:137px;font-size:13px;font-weight:700;line-height:17px">JOIN THE 12-WEEK<br>AMBER BROTH<br>QUEST</div>
  <div class="abs geo white" style="left:19px;top:192px;font-size:9px;font-weight:500">(WITH GUMMIES)</div>
  <div class="abs geo white" style="left:18px;top:218px;font-size:6px;writing-mode:vertical-rl;transform:rotate(180deg)">BEGINS</div>
  <div class="abs geo white" style="left:28px;top:216px;font-size:27px">MONDAY</div>
  <div class="abs geo white" style="left:18px;top:244px;font-size:27px">MAY 4TH</div>
  <div class="loss-band"><div class="loss-frame"><span class="loss-top">LOSE UP TO</span><div class="loss-main br">15LBS IN 10 DAYS!</div></div></div>
</section>

<!-- 7 -->
<section class="tile c1 r3">
  <div class="abs" style="left:0;right:0;top:0;height:282px;background:var(--paper)"></div>
  <div class="abs center cond dg tall" style="top:8px;font-size:32px;font-weight:500">SUMMER IS</div>
  <div class="abs cond dg tall" style="left:16px;top:44px;font-size:50px;font-weight:600">2 MONTHS</div>
  <div class="abs cond br" style="left:234px;top:50px;font-size:19px;font-weight:600;writing-mode:vertical-rl">AWAY!</div>
  <div class="abs" style="left:0;top:112px;width:122px;height:108px;background:var(--green-light)"></div>
  <div class="abs cond white" style="left:0;width:122px;text-align:center;top:118px;font-size:14px;font-weight:400">JOIN THE</div>
  <div class="abs cond white tall" style="left:0;width:122px;text-align:center;top:136px;font-size:29px;font-weight:600">12-WEEK</div>
  <div class="abs cond white" style="left:0;width:122px;text-align:center;top:176px;font-size:15px;font-weight:400;line-height:19px">AMBER BROTH<br>QUEST ON</div>
  <div class="abs cond bl tall" style="left:14px;top:230px;font-size:25px;font-weight:600">MAY 4TH!</div>
  <div class="book" role="img" aria-label="Cleanse recipe book cover" style="left:124px;top:118px;width:84px;height:150px"></div>
  <div class="bottle" role="img" aria-label="Gummies supplement bottle" style="left:210px;top:150px;width:48px;height:118px"></div>
  <div class="abs" style="left:0;right:0;top:272px;height:10px;background:var(--green-dark)"></div>
  <div class="loss-band"><div class="loss-frame"><span class="loss-top">LOSE UP TO</span><div class="loss-main bl">15LBS IN 10 DAYS!</div></div></div>
</section>

<!-- 8 -->
<section class="tile c2 r3">
  <div class="abs" style="left:30px;top:27px;width:40px;height:1px;background:#999"></div>
  <div class="abs" style="left:202px;top:27px;width:40px;height:1px;background:#999"></div>
  <div class="abs center cond dg tall" style="top:7px;font-size:30px;font-weight:600">GET YOUR</div>
  <div class="abs center cond dg tall" style="top:40px;font-size:62px;font-weight:700">SUMMER</div>
  <div class="abs center cond br tall" style="top:112px;font-size:44px;font-weight:600">BODY READY!</div>
  <div class="abs" style="left:18px;right:18px;top:173px;height:109px;border-radius:14px 14px 0 0;background:var(--green-light)"></div>
  <div class="abs center cond white" style="top:184px;font-size:14px;font-weight:400;line-height:18px">JOIN THE 12-WEEK AMBER BROTH<br>QUEST (WITH GUMMIES)</div>
  <div class="abs" style="left:18px;right:18px;top:230px;height:52px;border-radius:14px 14px 0 0;background:var(--brown)"></div>
  <div class="abs center cond white tall" style="top:243px;font-size:19px;font-weight:500">BEGINS MONDAY MAY 4TH</div>
  <div class="loss-band"><div class="loss-frame"><span class="loss-top bl">LOSE UP TO</span><div class="loss-main br">15LBS IN 10 DAYS!</div></div></div>
</section>

<!-- 9 -->
<section class="tile c3 r3">
  <div class="photo dots" role="img" aria-label="Host in polka-dot top smiling, pointing at gummies bottle" style="left:0;top:0;width:272px;height:282px;background:linear-gradient(160deg,#6f8a5a,#d9d3cf 45%,#2a2526)"></div>
  <div class="abs" style="left:18px;right:18px;top:174px;height:108px;border-radius:14px 14px 0 0;background:var(--green-light)"></div>
  <div class="abs center geo white" style="top:183px;font-size:15px;font-weight:700">SUMMER IS</div>
  <div class="abs center cond white" style="top:199px;font-size:30px;font-weight:600">2 MONTHS AWAY!</div>
  <div class="abs" style="left:18px;right:18px;top:238px;height:44px;border-radius:14px 14px 0 0;background:var(--brown)"></div>
  <div class="abs center cond white" style="top:243px;font-size:15px;font-weight:400;line-height:18px">JOIN THE 12-WEEK AMBER BROTH<br>QUEST ON <span class="lg">MAY 4TH!</span></div>
  <div class="loss-band"><div class="loss-frame"><span class="loss-top bl">LOSE UP TO</span><div class="loss-main br">15LBS IN 10 DAYS!</div></div></div>
</section>

</main>
</body>
</html>
```